RWT General Contracting

Roofing, Siding,windows, doors, Gutter,additions, decks, garagesand hanyman services fully insured and licensed, free estimates, accept all major credit cards call (617)442-9073 email morvinkt@mailbrook.net

Target Market(s)

Home improvement

Industry/Entity Type

Home Improvement

Requirements
Must have
• Whats listed above
Nice to have
• I dont have a logo i want wording for roofing, siding, gutter, decks, additions, windows, doors, and handyman services with my phone # 617-442-9073 and email morvinkt@mailbrook.net

```html
<!DOCTYPE html>
<html lang="en">
<head>
<meta charset="utf-8">
<title>RWT General Contracting – Postcard</title>
<link rel="stylesheet" href="https://fonts.googleapis.com/css2?family=Bebas+Neue&family=Lato:ital,wght@0,400;0,700;0,900;1,700&family=Oswald:wght@600&family=Libre+Baskerville:wght@400;700&family=Arimo&display=swap">
<style>
  :root {
    --page: #ecebe8;
    --navy: #13202e;
    --blue: #2a7dc4;
    --blue-bright: #3a9ae0;
    --blue-deep: #1b5f9e;
    --teal: #1f6fa8;
    --ink: #3b3d42;
    --grey-tab: #4a4f56;
    --white: #ffffff;
    --placeholder: #c3c3c3;
    --photo-sky: #a9c6d6;
    --photo-green: #5f7f3e;
    --photo-house: #8a8266;
  }
  * { box-sizing: border-box; margin: 0; padding: 0; }
  html, body { width: 907px; height: 1200px; overflow: hidden; }
  body { background: var(--page); position: relative; font-family: "Lato", sans-serif; }

  .card { position: absolute; left: 139px; width: 627px; background: var(--white); overflow: hidden; box-shadow: 0 2px 6px rgba(0,0,0,.25); }
  .card--front { top: 82px; height: 485px; }
  .card--back { top: 642px; height: 486px; }
  .abs { position: absolute; }

  /* front */
  .front-shapes { position: absolute; inset: 0; }
  .front-photo { position: absolute; inset: 0;
    clip-path: polygon(292px 0, 627px 0, 627px 262px, 376px 262px);
    background: linear-gradient(180deg, var(--photo-sky) 0%, #7f9b6a 35%, var(--photo-house) 60%, var(--photo-green) 100%); }
  .brand { left: 30px; top: 66px; display: flex; align-items: center; gap: 8px; white-space: nowrap;
    font: 700 17px/1 "Lato", sans-serif; color: var(--blue); }
  .brand__mark { width: 14px; height: 14px; background: var(--blue); }
  .tagline { left: 18px; top: 146px; font: 400 25px/1 "Bebas Neue", sans-serif; color: var(--blue-deep); letter-spacing: .3px; }
  .headline { left: 14px; top: 178px; font: 400 43px/1 "Bebas Neue", sans-serif; color: var(--ink); letter-spacing: .5px; }
  .services { left: 28px; top: 262px; width: 318px; height: 128px; border-radius: 10px;
    background: linear-gradient(180deg, var(--blue-bright), var(--blue-deep)); box-shadow: 0 3px 6px rgba(0,0,0,.3); }
  .services__title { left: 103px; top: 254px; width: 155px; height: 42px; background: var(--grey-tab);
    color: var(--white); font: 600 28px/42px "Oswald", sans-serif; text-align: center; box-shadow: 0 2px 4px rgba(0,0,0,.35); }
  .services__list { list-style: none; color: var(--white); font: 400 15.5px/19px "Lato", sans-serif; }
  .services__list li::before { content: "➤"; font-size: 10px; margin-right: 3px; vertical-align: 2px; }
  .services__list--a { left: 78px; top: 305px; }
  .services__list--b { left: 219px; top: 305px; }
  .cards-note { left: 31px; top: 412px; width: 281px; height: 38px; border-radius: 19px; background: var(--blue-deep);
    color: var(--white); font: italic 700 19px/38px "Lato", sans-serif; text-align: center; box-shadow: 0 3px 5px rgba(0,0,0,.35); }
  .badge { left: 434px; top: 234px; width: 128px; height: 128px; }
  .badge__text { left: 434px; top: 278px; width: 128px; text-align: center; color: var(--white);
    font: 600 14px/1.15 "Oswald", sans-serif; }
  .badge__text span { display: block; font-size: 20px; }
  .cta { right: 20px; top: 372px; text-align: right; color: var(--teal); font: 900 23px/29px "Lato", sans-serif; }
  .phone { right: 20px; top: 433px; display: flex; align-items: center; gap: 4px; color: var(--ink); font: 700 24px/1 "Lato", sans-serif; }
  .front-band { left: 0; bottom: 0; width: 100%; height: 19px; background: var(--navy); }

  /* back */
  .back-panel { position: absolute; inset: 0;
    clip-path: polygon(0 0, 344px 0, 273px 220px, 361px 486px, 0 486px); background: var(--blue); }
  .back-photo { left: 0; top: 0; width: 360px; height: 200px;
    background: linear-gradient(180deg, var(--photo-sky) 0%, #b8b48e 40%, var(--photo-house) 65%, var(--photo-green) 100%); }
  .back-header { left: 0; top: 200px; width: 360px; height: 40px; background: var(--navy); }
  .back-header__text { left: 16px; top: 213px; color: var(--white); font: 700 13.5px/1 "Libre Baskerville", serif; letter-spacing: .2px; }
  .back-footer { left: 0; top: 466px; width: 370px; height: 20px; background: var(--navy); }
  .message { left: 17px; top: 256px; width: 268px; }
  .pitch { color: var(--white); font: 400 12px/18px "Libre Baskerville", serif; white-space: nowrap; }
  .pitch b { font-weight: 700; }
  .pitch-strong { margin-top: 9px; color: var(--navy); font: 700 10.5px/15px "Libre Baskerville", serif; text-transform: uppercase; white-space: nowrap; }
  .thumb { top: 350px; width: 82px; height: 56px; border: 3px solid var(--white);
    background: linear-gradient(180deg, #9fb9cc, #8a6b5a 60%, #5e7a44); box-shadow: 0 1px 3px rgba(0,0,0,.4); }
  .contact { left: 19px; color: var(--white); font: 400 17px/1 "Arimo", sans-serif; display: flex; align-items: center; gap: 8px; }
  .contact--phone { top: 418px; }
  .contact--email { top: 442px; }
  .stamp-box { left: 475px; top: 20px; width: 135px; height: 135px; background: var(--placeholder); }
  .address-box { left: 332px; top: 180px; width: 278px; height: 175px; background: var(--placeholder); }
  .divider { position: absolute; inset: 0; }
</style>
</head>
<body>

<section class="card card--front">
  <svg class="front-shapes" width="627" height="485" viewBox="0 0 627 485">
    <polygon points="0,0 150,0 0,45" fill="#13202e"/>
    <polygon points="0,45 150,0 170,0 0,52" fill="#2a7dc4"/>
    <polygon points="255,0 290,0 372,262 342,262" fill="#13202e"/>
    <polygon points="280,0 298,0 384,270 627,270 627,278 366,278" fill="#2a7dc4"/>
  </svg>
  <div class="front-photo" role="img" aria-label="Photo of a two-storey house with porch, trees and flowering front garden"></div>

  <div class="abs brand"><span class="brand__mark"></span>RWT General Contracting</div>
  <p class="abs tagline">Residential Roofers &amp; Builders</p>
  <h1 class="abs headline">Have Water Damage?</h1>

  <div class="abs services"></div>
  <div class="abs services__title">SERVICES</div>
  <ul class="abs services__list services__list--a"><li>Roofing</li><li>Siding</li><li>Windows</li><li>Doors</li></ul>
  <ul class="abs services__list services__list--b"><li>Gutter</li><li>Additions</li><li>Decks</li><li>Garages</li></ul>

  <div class="abs cards-note">Accept all major credit cards</div>

  <svg class="abs badge" viewBox="0 0 128 128">
    <polygon fill="#2a7dc4" stroke="#ffffff" stroke-width="2" points="64,2 72,14 85,6 89,20 104,17 103,31 118,33 111,46 124,53 114,64 124,75 111,82 118,95 103,97 104,111 89,108 85,122 72,114 64,126 56,114 43,122 39,108 24,111 25,97 10,95 17,82 4,75 14,64 4,53 17,46 10,33 25,31 24,17 39,20 43,6 56,14"/>
  </svg>
  <div class="abs badge__text">FULLY INSURED<span>&amp; LICENSED</span></div>

  <p class="abs cta">CALL NOW FOR<br>YOUR FREE ESTIMATE</p>
  <p class="abs phone">
    <svg width="20" height="22" viewBox="0 0 24 24"><path fill="#1f6fa8" d="M6.6 10.8a15.1 15.1 0 0 0 6.6 6.6l2.2-2.2c.3-.3.7-.4 1-.2 1.1.4 2.3.6 3.6.6.6 0 1 .4 1 1V20c0 .6-.4 1-1 1A17 17 0 0 1 3 4c0-.6.4-1 1-1h3.5c.6 0 1 .4 1 1 0 1.3.2 2.5.6 3.6.1.3 0 .7-.2 1z"/></svg>
    (617)442-9073
  </p>
  <div class="abs front-band"></div>
</section>

<section class="card card--back">
  <div class="back-panel">
    <div class="abs back-photo" role="img" aria-label="Photo of a large suburban home with green lawn and landscaped front path"></div>
    <div class="abs back-header"></div>
    <div class="abs back-footer"></div>
  </div>
  <svg class="divider" width="627" height="486" viewBox="0 0 627 486">
    <polyline points="344,0 273,220 361,486" fill="none" stroke="#13202e" stroke-width="7"/>
  </svg>

  <p class="abs back-header__text">QUALITY ROOFING COMPANY</p>
  <div class="abs message">
    <p class="pitch"><b>Your home is the most important asset<br>you have,</b> so when your ready to remodel,</p>
    <p class="pitch-strong">Get yourself the best general<br>contractor in the business!</p>
  </div>

  <div class="abs thumb" style="left:17px" role="img" aria-label="Photo of a brick family home"></div>
  <div class="abs thumb" style="left:113px" role="img" aria-label="Photo of a red-brick house"></div>
  <div class="abs thumb" style="left:209px" role="img" aria-label="Photo of a terracotta-roofed home"></div>

  <p class="abs contact contact--phone">
    <svg width="16" height="16" viewBox="0 0 24 24"><path fill="#ffffff" d="M6.6 10.8a15.1 15.1 0 0 0 6.6 6.6l2.2-2.2c.3-.3.7-.4 1-.2 1.1.4 2.3.6 3.6.6.6 0 1 .4 1 1V20c0 .6-.4 1-1 1A17 17 0 0 1 3 4c0-.6.4-1 1-1h3.5c.6 0 1 .4 1 1 0 1.3.2 2.5.6 3.6.1.3 0 .7-.2 1z"/></svg>
    (617)442-9073
  </p>
  <p class="abs contact contact--email">
    <svg width="16" height="14" viewBox="0 0 24 20"><path fill="#ffffff" d="M2 2h20v16H2z"/><path fill="none" stroke="#2a7dc4" stroke-width="2" d="M2 3l10 8 10-8"/></svg>
    morvinkt@mailbrook.net
  </p>

  <div class="abs stamp-box"></div>
  <div class="abs address-box"></div>
</section>

</body>
</html>
```